Professional business cards for real estate development company

I need business cards for my new real estate development company. The company, "KORVA" is a real estate development, investment, and advisory firm with a focus on multifamily, office, and mixed-use projects across primary and secondary markets in the Southeast United States.

Style preference is modern

Industry/Entity Type

Real Estate Development

Contact Information for Business Card

The business cards need to include:
Name
Title
Mailing Address
Phone Number
Web Address

Logo is attached. I would like white to be the primary color with incorporation of the company colors: #232D3A and #B5A451

Font styles to use
Other font styles liked:
• Montserrat, Avenir

Requirements
Must have
• Company Logo. No need to include the company name since the name is in the logo.
Should not have
• No line type designs

```html
<!DOCTYPE html>
<html lang="en">
<head>
<meta charset="UTF-8">
<title>KORVA Business Cards</title>
<link rel="stylesheet" href="https://fonts.googleapis.com/css2?family=Roboto:wght@400;700&family=Montserrat:wght@600&display=swap">
<style>
  :root {
    --stage: #e9e8e6;
    --navy: #1f2a38;
    --navy-ink: #232d3a;
    --navy-soft: #2c3a4c;
    --paper: #ffffff;
    --text-muted: #555b63;
    --icon: #3a4250;
  }
  * { margin: 0; padding: 0; box-sizing: border-box; }
  html, body {
    width: 1200px; height: 795px; overflow: hidden;
    background: var(--stage);
  }
  .canvas {
    position: relative; width: 1200px; height: 795px;
  }
  .card {
    position: absolute; top: 243px;
    width: 540px; height: 309px;
    box-shadow: 0 6px 18px rgba(0,0,0,0.18);
  }
  .card--front { left: 40px; background: var(--navy); }
  .card--back { left: 620px; background: var(--paper); }

  .wordmark {
    font-family: "Montserrat", sans-serif;
    font-weight: 600;
    letter-spacing: 0.06em;
  }
  .card--front .wordmark {
    position: absolute; left: 0; right: 0; top: 50%;
    transform: translateY(-50%);
    text-align: center;
    font-size: 64px;
    color: var(--navy-soft);
  }
  .card--back .wordmark {
    position: absolute; left: 34px; top: 30px;
    font-size: 40px;
    color: var(--navy-ink);
  }

  .contact {
    position: absolute; left: 36px; top: 112px;
    font-family: "Roboto", sans-serif;
    font-size: 14px; line-height: 19px;
    color: var(--text-muted);
    list-style: none;
  }
  .contact__address { margin-bottom: 12px; }
  .contact__row { display: flex; align-items: center; gap: 6px; }
  .contact__row svg { width: 11px; height: 11px; fill: none; stroke: var(--icon); stroke-width: 1.6; }

  .person {
    position: absolute; right: 36px; top: 112px;
    text-align: right;
    font-family: "Roboto", sans-serif;
  }
  .person__name {
    font-size: 21px; font-weight: 700; color: var(--navy-ink);
    letter-spacing: 0.02em;
  }
  .person__title {
    font-size: 13px; color: var(--text-muted); margin-top: 2px;
  }
</style>
</head>
<body>
<main class="canvas">
  <section class="card card--front" aria-label="Card front">
    <div class="wordmark">KORVA</div>
  </section>

  <section class="card card--back" aria-label="Card back">
    <div class="wordmark">KORVA</div>

    <ul class="contact">
      <li class="contact__address">418 Alder Creek Rd<br>Marlow, GA 30312</li>
      <li class="contact__row">
        <svg viewBox="0 0 12 12"><path d="M2.5 1.5 L4.5 1.5 L5.2 4 L4 5 Q5 7.2 7 8 L8 6.8 L10.5 7.5 L10.5 9.5 Q10.5 10.5 9.5 10.5 Q1.5 10 1.5 2.5 Q1.5 1.5 2.5 1.5Z"/></svg>
        404-555-0148
      </li>
      <li class="contact__row">
        <svg viewBox="0 0 12 12"><rect x="1" y="2.5" width="10" height="7"/><path d="M1 2.5 L6 6.5 L11 2.5"/></svg>
        info@yourmailaddress.com
      </li>
      <li class="contact__row">
        <svg viewBox="0 0 12 12"><circle cx="6" cy="6" r="4.8"/><path d="M1.2 6 H10.8 M6 1.2 Q3.5 6 6 10.8 M6 1.2 Q8.5 6 6 10.8"/></svg>
        www.yourwebsite.com
      </li>
    </ul>

    <div class="person">
      <div class="person__name">DANA REYES</div>
      <div class="person__title">Founder &amp; CEO</div>
    </div>
  </section>
</main>
</body>
</html>
```